WORD Template for Training Manual called Lantern Road

I have written a training manual called Lantern Road. I need a design for the manual I can put the materials into for small groups of people to use.
This means a cover along with a page design that looks appealing but doesn't distract from the content.
We already have an organisational logo and colour scheme. It would be great to have at nine different page designs as the manual will have nine sessions of learning. So one design for each session of content.
I have uploaded some of the example materials we have designed from another designer as well so you can see the kind of look and feel our other materials have.
I have also uploaded the introduction and the first session of the content so you can use it to help shape the design.
As you will see in the sessions, each session has small group activities, discussion questions and a video content session for the group to watch. All nine sessions will be designed in a similar way.
There will also be a second booklet to design of daily reflections so a successful design for this workbook will lead to a second project with the same look and feel.
Updates
Need extra days to review
Target Market(s)
My target market is adults from 18-45
Industry/Entity Type
Christian Ministry
Look and feel
Each slider illustrates characteristics of the customer's brand and the style your logo design should communicate.

```html
<!DOCTYPE html>
<html lang="en">
<head>
<meta charset="utf-8">
<title>Lantern Road – Training Manual Pages</title>
<link href="https://fonts.googleapis.com/css2?family=Montserrat:wght@400;700;800&family=Open+Sans:ital,wght@0,400;0,600;1,600&family=Parisienne&display=swap" rel="stylesheet">
<style>
:root{
  --backdrop:#c9c9c9;
  --cover-blue:#4062b4;
  --ink:#3b3b3b;
  --lime:#a6c53a;
  --sky:#8bbad3;
  --violet:#5b4a9e;
  --violet-soft:#8e7fc4;
  --plum:#574c69;
  --royal:#3f5db0;
  --white:#ffffff;
}
*{margin:0;padding:0;box-sizing:border-box}
html,body{width:1200px;height:2374px;overflow:hidden;background:var(--backdrop)}
body{position:relative;font-family:"Open Sans",Arial,sans-serif;color:var(--ink)}
.page{position:absolute;width:452px;height:640px;overflow:hidden;background:var(--white)}
.page > *{z-index:2}
.page > .art,.page > .wash{z-index:1}
.page--cover{left:90px;top:140px;background:var(--cover-blue)}
.page--intro{left:659px;top:140px}
.page--intro-cont{left:90px;top:855px}
.page--session{left:659px;top:855px;background:var(--sky)}
.page--video{left:90px;top:1571px}
.page--discussion{left:659px;top:1571px;background:var(--plum);color:var(--white)}
.folio{position:absolute;right:40px;top:42px;font-size:7.5px;color:#555}
.page--discussion .folio{color:#e6e2ee}
.wash{position:absolute;border-radius:50%;filter:blur(22px);opacity:.55}
.body-copy{position:absolute;left:44px;width:364px;font-size:7.9px;line-height:1.45;text-align:justify}
.body-copy p{margin-bottom:10px}
.art{position:absolute}

/* cover */
.brand{position:absolute;right:36px;top:42px;display:flex;align-items:center;gap:8px;font-weight:600;font-size:26px;color:var(--white)}
.brand i{width:16px;height:16px;border-radius:50%;background:var(--white);display:block}
.cover-title{position:absolute;left:28px;top:126px;font-family:Montserrat,sans-serif;font-weight:800;font-size:27px;color:var(--white);letter-spacing:.5px}
.cover-sub{position:absolute;left:28px;top:180px;width:230px;font-family:Montserrat,sans-serif;font-size:13.2px;line-height:1.3;color:var(--white)}
.cover-url{position:absolute;right:36px;bottom:26px;font-family:Montserrat,sans-serif;font-size:13px;color:var(--white);letter-spacing:.3px}

.h-intro{position:absolute;left:44px;top:104px;font-size:23px;font-weight:600;color:var(--lime)}

/* session */
.week-tag{position:absolute;left:44px;top:38px;height:23px;width:108px;background:var(--violet);color:var(--white);border-radius:0 12px 12px 0;font-size:10px;padding-left:38px;line-height:23px}
.week-tag .cal{position:absolute;left:0;top:-1px;width:28px;height:30px;background:#fff;border:2px solid var(--violet)}
.script{font-family:Parisienne,cursive}
.session-title{position:absolute;left:112px;top:100px;font-size:22px;font-weight:400;color:var(--white)}
.topic{position:absolute;left:44px;top:138px;width:364px;font-size:7.9px;line-height:1.45;color:var(--white);text-align:justify}
.topic b{color:var(--violet);font-weight:600}
.lead{position:absolute;left:44px;font-size:7.9px;color:var(--white)}
.outcome{position:absolute;left:40px;right:0;height:18px;border-radius:9px 0 0 9px;background:linear-gradient(90deg,var(--violet) 0%,var(--violet-soft) 70%,rgba(142,127,196,0) 100%);color:var(--white);font-size:7.8px;line-height:18px;padding-left:34px}
.outcome .num{position:absolute;left:0;top:-1px;width:20px;height:20px;border-radius:50%;background:var(--white);border:1.5px solid var(--violet);color:var(--violet);font-size:7px;text-align:center;line-height:17px}
.resource{position:absolute;left:44px;top:268px;font-size:7.5px;font-style:italic;font-weight:600;color:var(--violet);padding-left:24px}
.resource svg{position:absolute;left:0;top:-3px}
.pill{position:absolute;left:44px;top:291px;height:16px;padding:0 24px 0 12px;border-radius:8px;background:var(--violet);color:var(--white);font-size:10px;line-height:16px}
.pill svg{position:absolute;right:5px;top:2px}

/* video page */
.video-head{position:absolute;left:30px;top:90px;font-size:15px;font-weight:600;color:var(--lime);display:flex;align-items:baseline;gap:4px}
.video-head .script{font-size:24px;font-weight:400;color:var(--lime)}
.sec-head{position:absolute;left:45px;font-size:11px;font-weight:600;color:var(--royal);display:flex;align-items:center;gap:8px}
.sec-head.lime{color:var(--lime)}
.bullets{position:absolute;left:54px;width:354px;font-size:7.9px;line-height:1.45;list-style:none}
.bullets li{position:relative;margin-bottom:6px}
.bullets li::before{content:"";position:absolute;left:-8px;top:4px;width:3.5px;height:3.5px;border-radius:50%;background:var(--lime)}
.timeline{position:absolute;width:1.5px;background:var(--lime)}
.step{position:absolute;width:15px;height:15px;border-radius:50%;background:var(--lime);border:2px solid rgba(255,255,255,.6);font-size:7.5px;line-height:11px;text-align:center;color:#35402a;font-weight:600}
.tick{position:absolute;height:1px;background:var(--lime)}
.note{position:absolute;font-size:7.9px;line-height:1.45}
</style>
</head>
<body>

<!-- Cover -->
<section class="page page--cover">
  <div class="art" role="img" aria-label="Illustration of open hands releasing a red bird among deep blue leaves and branches" style="left:20px;top:250px;width:420px;height:340px;border-radius:50%;background:radial-gradient(ellipse at 66% 34%,#e8593f 0 14%,#b9d9ea 15% 28%,#3554a6 48%,rgba(64,98,180,0) 72%)"></div>
  <div class="brand"><i></i>Hearthway</div>
  <h1 class="cover-title">LANTERN ROAD</h1>
  <p class="cover-sub">60 Days of learning that will teach you to leap from safety into the adventure of your life!</p>
  <p class="cover-url">www.hearthway.org.au</p>
</section>

<!-- Introduction -->
<section class="page page--intro">
  <div class="wash" style="left:-30px;top:-40px;width:240px;height:90px;background:#d8ea7c"></div>
  <div class="wash" style="right:-30px;top:40px;width:140px;height:90px;background:#a9dcef"></div>
  <p class="folio">www.hearthway.org.au &nbsp;|&nbsp; 1</p>
  <h2 class="h-intro">Introduction</h2>
  <div class="body-copy" style="top:158px">
    <p>When I was a young boy, I loved games and adventures. Games I played with Mum and Dad, and the adventures I read in books or created in my imagination and played out in the backyard. One of my favourite games was pretty simple. I would start at the end of the hallway in our house, Mum would call me, and I would run down the hallway as fast as I could. When I got to the end of the hallway, I would leap into the air through the doorway into the kitchen, and she would catch me and give me a great big hug.</p>
    <p>One day I put my fertile imagination and this game together and decided to play the game with Dad. Dad came home from work one afternoon through the front door and headed down the hallway to the kitchen. He stood in the kitchen in clear view and was chatting with Mum. I imagined what it would be like to play this game with Dad; in my head, it all played out beautifully.</p>
    <p>So, I yelled out, “Dad, Dad, ”and took off down the hallway as fast as my legs could carry me. Dad had a look in my direction and then looked back to Mum. I kept running down the hallway, and Dad looked back at me and waited for me to arrive; I got to the Kitchen doorway and leapt as high and as far as I had ever jumped in my life...</p>
  </div>
  <div class="art" role="img" aria-label="Decorative botanical illustration with leaves, dots and soft blobs in mustard, blush, slate and indigo" style="left:0;top:385px;width:452px;height:255px;background:linear-gradient(180deg,rgba(255,255,255,0) 0%,#e9c9b4 30%,#c9c36a 55%,#8fa3ae 78%,#5a64b8 100%);border-radius:46% 54% 0 0/30% 30% 0 0"></div>
</section>

<!-- Introduction continued -->
<section class="page page--intro-cont">
  <div class="wash" style="left:-40px;top:-10px;width:120px;height:160px;background:#fde08a"></div>
  <div class="wash" style="right:-20px;top:-30px;width:220px;height:80px;background:#f9c3cf"></div>
  <p class="folio">www.hearthway.org.au &nbsp;|&nbsp; 2</p>
  <div class="body-copy" style="top:140px">
    <p>I regained consciousness with blood running down my face and my dad saying, “I didn’t know the game”. Mum was trying to stop the bleeding, and my brain was struggling to figure out what had happened. It seems I had flown across the kitchen headfirst into the cupboards, cutting my head open on the cupboard door handle, a scar I retain to this day.</p>
    <p>For me, following Jesus can be a little like this, I think I have it figured out, and I embark on what I think God wants me to do; I hit my head and then wonder what on earth happened. At that point, wounded and bruised, God always brings me back to the basics. He calls me back to his simple commands to love others the way he loves me, to announce that He is here, that He loves others too, and to gather with other followers for worship, encouragement and support so we can follow Jesus together.</p>
    <p>Lantern Road takes followers of Jesus through those basic commands and their implications for our everyday life. My goal in developing this material is to teach you how to look at the world around you through Jesus’ eyes, to see people the way He sees them, and then to pursue His mission as a part of your everyday being and doing. To move beyond believing in God and accepting His Grace and Forgiveness to living his commands faithfully and, by doing so, being part of God’s transformation project, just like He always intended.</p>
  </div>
  <div class="art" role="img" aria-label="Colourful flower garden illustration in pink, orange, yellow and green" style="left:0;top:400px;width:452px;height:240px;background:linear-gradient(180deg,rgba(255,255,255,0) 0%,#f6a8bf 35%,#f8b23c 62%,#2e9b5c 100%)"></div>
</section>

<!-- Week One session -->
<section class="page page--session">
  <div class="week-tag"><span class="cal"></span>Week One</div>
  <p class="folio" style="color:#f1f6fa">www.hearthway.org.au &nbsp;|&nbsp; 3</p>
  <h2 class="session-title script">What is Love ?</h2>
  <p class="topic"><b>Topic:</b> Love is a choice, followed by an action to step into the world of another and act self-sacrificially in that person’s best interests.</p>
  <p class="lead" style="top:169px">In this session, participants will learn to:</p>
  <div class="outcome" style="top:190px"><span class="num">01</span>Explain the biblical concept of Love as expressed by God through Jesus Christ.</div>
  <div class="outcome" style="top:221px"><span class="num">02</span>Describe how they can express love towards others in their context.</div>
  <p class="lead" style="top:250px">Resources you will need:</p>
  <p class="resource"><svg width="16" height="14" viewBox="0 0 16 14"><rect x="3" y="1" width="11" height="12" fill="none" stroke="#fff" stroke-width="1"/><rect x="1" y="3" width="11" height="10" fill="none" stroke="#fff" stroke-width="1"/></svg>A3 Paper for drawing and Coloured Pencils/Text as for drawing.</p>
  <div class="pill">Pre-video activity<svg width="12" height="12" viewBox="0 0 12 12"><circle cx="6" cy="6" r="5" fill="none" stroke="#fff"/><path d="M5 3.5 8 6 5 8.5z" fill="#fff"/></svg></div>
  <p class="topic" style="top:313px">In groups of 3, draw a picture representing the moment the father welcomes his prodigal son home (Luke 15:11-32). Think about what it was the father was saying through his actions. What was the son saying through his actions? What was being expressed between them? This is not a picture of the moment like a photograph, but rather a picture representing it in a way that might not even have the father and son in it.</p>
  <div class="art" role="img" aria-label="Collage illustration of a reaching hand, a bird in a cloud, and a thoughtful figure among bright foliage" style="left:0;top:375px;width:452px;height:265px;background:linear-gradient(160deg,rgba(139,186,211,0) 0%,#f3ead8 20%,#ef6a3a 48%,#1f5aa8 72%,#143d7a 100%);border-radius:40% 60% 0 0/25% 30% 0 0"></div>
</section>

<!-- Video content page -->
<section class="page page--video">
  <div class="wash" style="left:-40px;top:40px;width:90px;height:220px;background:#cfc3ee"></div>
  <div class="wash" style="right:-30px;top:20px;width:90px;height:150px;background:#bfe3a0"></div>
  <p class="folio">www.hearthway.org.au &nbsp;|&nbsp; 4</p>
  <h2 class="video-head">Show Video Content for <span class="script">What is Love ?</span></h2>
  <h3 class="sec-head" style="top:133px"><svg width="26" height="14" viewBox="0 0 26 14"><g fill="#3f5db0"><circle cx="5" cy="4" r="2.5"/><circle cx="13" cy="3.5" r="2.8"/><circle cx="21" cy="4" r="2.5"/><rect x="1.5" y="7" width="7" height="7" rx="2"/><rect x="9.5" y="7" width="7" height="7" rx="2"/><rect x="17.5" y="7" width="7" height="7" rx="2"/></g></svg>Large Group Discussion</h3>
  <ul class="bullets" style="top:160px">
    <li>Was there any content in the video that was new to you or expressed in a way that you hadn’t heard before?</li>
    <li>What were the key points being made in the video?</li>
  </ul>
  <div class="art" role="img" aria-label="Illustration of four people talking around a table with speech bubbles and plants" style="left:44px;top:242px;width:364px;height:176px;border-radius:50% 50% 12px 12px/40% 40% 12px 12px;background:linear-gradient(180deg,#eef2fb 0%,#c9d6f0 45%,#5b7cc4 75%,#3aa05a 100%)"></div>
  <h3 class="sec-head" style="top:458px"><svg width="14" height="16" viewBox="0 0 14 16"><g fill="#3f5db0"><circle cx="4" cy="3" r="2.3"/><circle cx="10" cy="3" r="2.3"/><rect x="1" y="6" width="6" height="10" rx="2"/><rect x="7" y="6" width="6" height="10" rx="2"/></g></svg>Small Group Discussion</h3>
  <p class="note" style="left:45px;top:481px">In groups of three, discuss the following questions.</p>
  <div class="timeline" style="left:21px;top:510px;height:130px"></div>
  <div class="step" style="left:14px;top:503px">1</div>
  <p class="note" style="left:45px;top:501px;width:362px">When Jesus was born, God entered our world. God incarnate, God in human flesh. This is the moment God’s revolution began when God chose to enter and dwell amongst us. This is the heart of God’s mission, to go and live with His created humans.</p>
  <div class="tick" style="left:22px;top:547px;width:26px"></div>
  <ul class="bullets" style="top:541px"><li>What does it mean to you that God wants to live in your world and understand what life is like for you?</li></ul>
</section>

<!-- Discussion continued -->
<section class="page page--discussion">
  <p class="folio">www.hearthway.org.au &nbsp;|&nbsp; 5</p>
  <div class="timeline" style="left:25px;top:80px;height:560px"></div>
  <div class="step" style="left:18px;top:74px">2</div>
  <p class="note" style="left:44px;top:72px;width:364px;text-align:justify">In doing this, God has expressed His love for each and every person He has created. Paul expressed this best in Romans 5:6-8, writing, “You see, just at the right time, when we were still powerless, Christ died for the ungodly. Very rarely will anyone die for a righteous person, though for a good person, someone might possibly dare to die. But God demonstrates his own love for us in this: While we were still sinners, Christ died for us.”</p>
  <div class="tick" style="left:26px;top:147px;width:26px"></div>
  <div class="tick" style="left:26px;top:165px;width:26px"></div>
  <ul class="bullets" style="top:141px;left:62px;width:346px">
    <li>What does it mean to you that God’s love for you is something you haven’t and can’t earn?</li>
    <li>What example does that set for each of us in how we love others?</li>
  </ul>
  <div class="step" style="left:18px;top:186px">3</div>
  <p class="note" style="left:44px;top:186px;width:364px">To love someone means choosing to enter into their world in the same way that God entered into our world. Once we have chosen to do this, we pick up our cross and prepare to sacrifice our self-interests to benefit the other person whom Jesus loves.</p>
  <div class="tick" style="left:26px;top:231px;width:26px"></div>
  <div class="tick" style="left:26px;top:259px;width:26px"></div>
  <ul class="bullets" style="top:225px;left:62px;width:346px">
    <li>What might this look like in practical terms? Is there an example of this you could think of and share?</li>
    <li>What are some of the potential costs of living this way?</li>
  </ul>
  <div class="step" style="left:18px;top:279px">4</div>
  <p class="note" style="left:44px;top:280px">Read Romans 5:1-5.</p>
  <div class="tick" style="left:26px;top:304px;width:26px"></div>
  <ul class="bullets" style="top:298px;left:62px;width:346px"><li>Does anyone have an example to share of their decision to love someone causing personal suffering? Can you relate to what Paul has written about suffering leading to resilience, character, and hope?</li></ul>
  <h3 class="sec-head lime" style="top:350px;left:44px"><svg width="26" height="14" viewBox="0 0 26 14"><g fill="#a6c53a"><circle cx="5" cy="4" r="2.5"/><circle cx="13" cy="3.5" r="2.8"/><circle cx="21" cy="4" r="2.5"/><rect x="1.5" y="7" width="7" height="7" rx="2"/><rect x="9.5" y="7" width="7" height="7" rx="2"/><rect x="17.5" y="7" width="7" height="7" rx="2"/></g></svg>Large Group Discussion</h3>
  <p class="note" style="left:44px;top:372px;width:364px">Share with the larger group what your group has learned together as you have worked through the questions.</p>
  <p class="note" style="left:44px;top:402px">Close the evening with a time of prayer.</p>
  <div class="art" role="img" aria-label="Collage illustration of a woman holding a cup among clouds, flowers and leaves in orange, blue and cream" style="left:0;top:428px;width:452px;height:212px;background:linear-gradient(170deg,rgba(87,76,105,0) 0%,#f2efe8 22%,#e8582f 48%,#2f5ea8 72%,#9cc7df 100%);border-radius:30% 40% 0 0/20% 25% 0 0"></div>
</section>

</body>
</html>
```